Vorsa -Letter Head

We are predominantly a residential home builder based in Melbourne, Victoria Australia. We construct houses, apartments, townhouses, multi-unit developments.

The name of the company is "Vorsa"
My company believes in building unique construction projects mainly residential homes. The target customers are upmarket Melbourne residents/investors.

I want the brand name "Vorsa" to be part of the logo. There's no need to put the word construction in the logo at this stage.

I would also like some ideas for a slogan. But I would like something unique and different for a slogan not the same old cliche.

Industry/Entity Type

Construction

Requirements
Must have
• I need to be able to print quotes, general letters for customers, print tables and pictures on the letter head. So it must not have too much graphics and should be simple.

```html
<!DOCTYPE html>
<html lang="en">
<head>
<meta charset="utf-8">
<title>Vorsa Letterhead</title>
<link rel="stylesheet" href="https://fonts.googleapis.com/css2?family=Comfortaa:wght@700&display=swap">
<style>
  :root {
    --brand-cyan: #1bbbe8;
    --rule-cyan: #c4eef9;
    --arc-tint: #e1f5fb;
    --paper: #ffffff;
  }
  html, body {
    margin: 0;
    padding: 0;
    overflow: hidden;
    background: var(--paper);
  }
  .letterhead {
    position: relative;
    width: 848px;
    height: 1200px;
    background: var(--paper);
    overflow: hidden;
  }
  .brand {
    position: absolute;
    left: 32px;
    top: 38px;
    display: flex;
    align-items: center;
    gap: 8px;
    font-family: "Comfortaa", sans-serif;
    font-weight: 700;
    font-size: 40px;
    line-height: 1;
    color: var(--brand-cyan);
    letter-spacing: 1px;
  }
  .brand-mark {
    width: 14px;
    height: 14px;
    background: var(--brand-cyan);
  }
  .header-rule {
    position: absolute;
    left: 166px;
    right: 0;
    top: 66px;
    height: 3px;
    background: var(--rule-cyan);
  }
  .footer-arc {
    position: absolute;
    left: 0;
    top: 0;
  }
</style>
</head>
<body>
  <main class="letterhead">
    <div class="brand"><span class="brand-mark"></span>Vorsa</div>
    <div class="header-rule"></div>
    <svg class="footer-arc" width="848" height="1200" viewBox="0 0 848 1200" aria-hidden="true">
      <path d="M0 1200 A424 398 0 0 1 848 1200 L670 1200 A246 222 0 0 0 178 1200 Z" fill="var(--arc-tint)"/>
    </svg>
  </main>
</body>
</html>
```